Company Brochure / Sales Sheet

We would like a brochure that we will may print out as well as forward electronically to our prospective clients.

Our clients are inventors/doctors/surgeons of medical products who need help completing their medical product, gaining approval, and then selling their product into the US market

Target Market(s)

Inventors of medical products who want to sell them in the United States

Industry/Entity Type

Medical

Font styles to use
Serif
Sans Serif

Requirements
Must have
• The word "Medical" should not receive special empahsis.
• Use the last two photos and whatever other photos that look good. You can edit and crop the photos
• Text should be easy to read
Nice to have
• We want to show that we have a lot of products.
• Sharp, clean, modern
• Minimum two pages - final product should be capable of being printed and
• forwarded electronically
• Easy to read
Should not have
• Should not be cluttered

```html
<!DOCTYPE html>
<html lang="en">
<head>
<meta charset="utf-8">
<title>Meridian Care Partners – Sales Sheet</title>
<link rel="stylesheet" href="https://fonts.googleapis.com/css2?family=Fira+Sans:wght@300;400;500;600&family=Roboto:wght@700&family=Bitter:wght@400;700&display=swap">
<style>
  :root {
    --ink: #2b2b2b;
    --text: #3c3c3c;
    --muted: #555555;
    --yellow: #fcc72a;
    --band: #efeeed;
    --white: #ffffff;
    --dots: #555555;
    --accent: #b3232a;
  }
  * { margin: 0; padding: 0; box-sizing: border-box; }
  html, body { width: 855px; height: 1200px; overflow: hidden; background: var(--white); }
  .sheet { position: relative; width: 855px; height: 1200px; font-family: "Fira Sans", sans-serif; color: var(--text); }

  .brand { position: absolute; left: 45px; top: 52px; display: flex; align-items: center; gap: 10px; }
  .brand-dot { width: 34px; height: 34px; border-radius: 50%; background: var(--accent); }
  .brand-name { font-family: "Fira Sans", sans-serif; font-weight: 600; font-size: 19px; letter-spacing: 0.5px; color: var(--ink); line-height: 1.1; }

  .contact { position: absolute; left: 520px; top: 50px; width: 270px; text-align: center; font-size: 12px; letter-spacing: 1.4px; color: var(--muted); line-height: 23px; font-weight: 300; }

  .hero { position: absolute; left: 0; top: 138px; width: 855px; height: 420px;
    background: radial-gradient(ellipse at 75% 15%, #c9d0bf 0%, rgba(201,208,191,0) 45%),
                radial-gradient(ellipse at 55% 80%, #4b86a8 0%, rgba(75,134,168,0) 55%),
                linear-gradient(120deg, #24483f 0%, #3a6362 35%, #3f7c9c 65%, #2f4d5c 100%); }
  .headline { position: absolute; left: 270px; font-family: "Roboto", sans-serif; font-weight: 700; font-size: 30px; letter-spacing: -1.2px; color: var(--ink); background: var(--yellow); line-height: 1; padding: 10px 9px; white-space: nowrap; }
  .headline.one { top: 197px; width: 253px; }
  .headline.two { top: 247px; width: 484px; }
  .tagline { position: absolute; left: 270px; top: 297px; width: 484px; height: 78px; background: rgba(255,255,255,0.6); padding: 4px 11px; font-size: 18.5px; line-height: 23.5px; color: var(--ink); font-weight: 400; white-space: nowrap; }

  .about { position: absolute; left: 0; top: 558px; width: 855px; height: 248px; background: var(--band); }
  .about-kicker { position: absolute; left: 48px; top: 88px; font-size: 13px; color: var(--ink); }
  .about-title { position: absolute; left: 46px; top: 102px; font-family: "Roboto", sans-serif; font-weight: 700; font-size: 38px; letter-spacing: -0.5px; color: var(--ink); }
  .about-rule { position: absolute; left: 231px; top: 58px; height: 106px; border-left: 2px dotted var(--dots); }
  .about-copy { position: absolute; left: 269px; top: 19px; width: 535px; font-size: 11.6px; line-height: 15.1px; font-weight: 300; color: var(--text); }
  .about-copy p + p { margin-top: 15px; }

  .callout { position: absolute; left: 44px; top: 825px; width: 213px; height: 296px; background: var(--yellow); padding: 21px 6px 0 26px; color: var(--ink); }
  .callout-text { font-size: 13.2px; line-height: 16.8px; font-weight: 300; white-space: nowrap; }
  .callout-bar { display: block; margin-top: 10px; width: 44px; height: 3px; background: var(--ink); }
  .callout-tail { position: absolute; left: 72px; top: 1120px; }

  .feature { position: absolute; }
  .feature h2 { font-family: "Bitter", serif; font-weight: 400; font-size: 20px; line-height: 20px; color: var(--ink); }
  .feature h2 b { font-weight: 700; }
  .feature p { font-size: 11.6px; line-height: 15.2px; font-weight: 300; color: var(--text); }
  .feature p + p { margin-top: 15px; }
  .feature svg { position: absolute; }

  .products { left: 298px; top: 823px; width: 172px; }
  .products h2 { margin-left: 24px; }
  .products p:first-of-type { margin-top: 24px; }

  .ip { left: 507px; top: 820px; width: 300px; }
  .ip h2 { margin-left: 51px; }
  .ip p { margin-top: 20px; }

  .regulatory { left: 507px; top: 998px; width: 300px; }
  .regulatory h2 { margin-left: 50px; padding-top: 12px; }
  .regulatory p { margin-top: 27px; }

  .col-rule { position: absolute; left: 487px; top: 820px; height: 340px; border-left: 2px dotted var(--dots); }
  .row-rule { position: absolute; left: 528px; top: 977px; width: 214px; border-top: 2px dotted var(--dots); }

  .foot-band { position: absolute; left: 0; top: 1181px; width: 855px; height: 19px; background: var(--band); }
</style>
</head>
<body>
<main class="sheet">
  <header>
    <div class="brand">
      <span class="brand-dot"></span>
      <span class="brand-name">MERIDIAN CARE<br>PARTNERS</span>
    </div>
    <div class="contact">(555) 014-2280<br>meridiancarepartners.com</div>
  </header>

  <section class="hero" role="img" aria-label="Photo of a gloved surgeon's hand over surgical instruments laid on a blue drape"></section>
  <h1 class="headline one">SAVING LIVES &amp;</h1>
  <div class="headline two">REDUCING HEALTH CARE COSTS</div>
  <p class="tagline">We are passionate about completing promising<br>medical technology projects and improving patient<br>lifestyles with our services.</p>

  <section class="about">
    <div class="about-kicker">LET’S TALK</div>
    <h2 class="about-title">About Us</h2>
    <div class="about-rule"></div>
    <div class="about-copy">
      <p>We are a network of medical distribution professionals including physicians and surgeons, regulatory and coding experts, patent and trademark lawyers, international fulfillment experts, marketing and advertising professionals, and business strategists all working together in the distribution of promising new medical products. We handle all aspects of new medical and surgical product sales, marketing, and distribution.</p>
      <p>Our company was founded in Milford, Delaware, with distribution locations and support associates and affiliates located throughout the United States. We have extensive experience with medical product development, intellectual property, and regulatory and compliances issues.</p>
      <p>We partner with medical innovators by providing strategic support with intellectual property and regulatory approval, reimbursement coding, marketing, selling and distributing state of the art medical products. Our clients include highly creative medical companies with strong management teams and consumer-driven growth perspectives.</p>
    </div>
  </section>

  <aside class="callout">
    <p class="callout-text">Our products are uniquely<br>positioned in an evolving<br>health sector to offer bene-<br>fits to patients, health care<br>institutions, medical profes-<br>sionals, insurance compa-<br>nies and governmental<br>agencies. Our evi-<br>dence-based technologies<br>reduce overall health care<br>expenses and empower<br>physicians and surgeons to<br>provide improved practices<br>and standards of care.</p>
    <span class="callout-bar"></span>
  </aside>
  <svg class="callout-tail" width="45" height="54" viewBox="0 0 45 54"><polygon points="5,0 45,0 0,54" fill="#fcc72a"/></svg>

  <article class="feature products">
    <svg width="14" height="42" viewBox="0 0 14 42" style="left:0;top:2px"><circle cx="7" cy="6" r="5" fill="none" stroke="#2b2b2b" stroke-width="1.8"/><circle cx="7" cy="6" r="1.6" fill="#2b2b2b"/><rect x="4.5" y="12" width="5" height="28" rx="1" fill="none" stroke="#2b2b2b" stroke-width="1.8"/><line x1="7" y1="24" x2="7" y2="36" stroke="#2b2b2b" stroke-width="1.5"/></svg>
    <h2>Medical<br><b>Products</b></h2>
    <p>We specialize in the distribution of next generation medical products including customized surgical instruments and kits, monitoring and diagnostic devices, advanced wound care products and innovative acute care disposables.</p>
    <p>Our medical products represent breakthroughs in medical technology, saving lives, reducing healthcare costs and improving patient lifestyles.</p>
  </article>

  <div class="col-rule"></div>

  <article class="feature ip">
    <svg width="40" height="34" viewBox="0 0 40 34" style="left:1px;top:5px"><g fill="none" stroke="#2b2b2b" stroke-width="1.7" stroke-linejoin="round"><polygon points="20,2 38,10 20,18 2,10"/><polyline points="2,17 20,25 38,17"/><polyline points="2,24 20,32 38,24"/></g></svg>
    <h2>Intellectual Property<br><b>&amp; Branding</b></h2>
    <p>Our team of patent attorneys and agents is effective and affordable and has gained more than 300 client patent approvals. We help our clients brand and position their products for successful product launches and introductions to the U.S. market.</p>
  </article>

  <div class="row-rule"></div>

  <article class="feature regulatory">
    <svg width="40" height="38" viewBox="0 0 40 38" style="left:1px;top:0"><g fill="none" stroke="#2b2b2b" stroke-width="1.6" stroke-linejoin="round"><polygon points="1,15 13,24 1,33"/><line x1="20" y1="12" x2="20" y2="36"/><polygon points="39,15 27,24 39,33"/><path d="M8,10 Q20,-2 32,10"/><polyline points="29,6 32,10 28,12"/></g></svg>
    <h2>Regulatory <b>Issues</b></h2>
    <p>We provide comprehensive services support for global physician inventors who are seeking to distribute their medical products within the United States. We assist in navigating the unique aspects of the US medical market — including FDA compliance and device returns, U.S. Customs, and reimbursement coding.</p>
  </article>

  <div class="foot-band"></div>
</main>
</body>
</html>
```